VRUM Diagnostics App - zOS

I need some UI artwork (2D) for my already released zOS app: "VRUM Kv" I'd like the UI to look more like an in-dash head-unit in a car. I'm in the process of updating the app with Tabro support and would like to release this next version with a brand new UI.

A lot of car audio enthusiast already use my app and probably mount their Pellix/Pello near their car audio components on the dash. Most of the car audio deck Mfgs support a few colors: Green/Blue/Amber/Red I'd like to offer these themes as well. But I will settle for the Amber color to match my existing App icon scheme. (nice to have)

My UI is incredibly simple. It's just a bunch of up/down buttons. I plan to do some animations an will need some room blocked off for this to the left of LCD text.

Screenshots are of my existing zOS app for Pellix and the half assed job I did for Tabro. - Note: These are the only two orientations I plan to use. But the resolution in these photos are smaller than my requirements. See "Must Haves" for all four resolutions.

update: I'd like something to imitate the style of the skin in the following: http://quorvel.artmosaicnet.example/art/Plomtune-KXP14-Skin-71824069

Thanks!

Target Market(s)

Car Audio Enthusiasts

Industry/Entity Type

Audio

Requirements
Must have
• - Static background that looks like an in-dash stereo. (think plomtune skin)
- An LCD area where I can display some text and stats on left (see Tabro ss)
- UI buttons that support up/down states. When the user presses a button, it stays "down" until it's tapped again or another is pushed.
- UI toggle switch for Wobble mode (see ss)

Pellix/Pello resolutions
-
- Landscape for Pellix4/4T Clarion (960 x 640)
- Landscape for Pellix 5 Clarion (1136 x 640)

Tabro resolutions
-
- This UI has more buttons and taller, but I'd like a similar look and feel
- Landscape for Tabro Clarion (2048 x 1536)
- Landscape for Tabro2/lite (1024 x 768)

Other Controls:
- An empty space for UI slider control. I will place this over artwork. (see ss)
- Emergency stop button should be red and easily accessible. Slightly larger than other buttons.

Pellix Buttons/Controls
-
20,30,40,50,60,70,80,90,100,150,250,300
Toggle Switch, P button, S button, Stop button

Tabro Buttons/Controls
-
20,25,30,35,40,45,50,55,60,65,70,80,90,110,125,150,250,300
Instant VRUM Buttons: 20,25,30,35,40,45,50,55

Disregard the waveform animation in the screenshots (squiggly line at bottom) I plan do a small animation to the left of the text in the LCD area.
Nice to have
• - Theme for LED-like colors: Green/Blue/Amber/Red on-off buttons
Should not have
• - sharp corners on buttons
- stretched version of Pellix layout for the Tabro.

```html
<!DOCTYPE html>
<html lang="en">
<head>
<meta charset="utf-8">
<title>VRUM Kv</title>
<link href="https://fonts.googleapis.com/css2?family=Arimo:wght@700&family=Orbitron:wght@500;700&display=swap" rel="stylesheet">
<style>
  :root{
    --bg-top:#141414;
    --bg-bottom:#2b2b2b;
    --ink:#0b0b0b;
    --white:#ffffff;
    --lcd:#fff33c;
    --lcd-grid:rgba(80,70,0,.45);
    --frame:#4a4a4a;
    --key-top:#fff9a8;
    --key-mid:#ffe94a;
    --key-low:#f9b02a;
    --key-line:#f29b10;
    --active-top:#e8331c;
    --active-low:#f79a1e;
    --stop-top:#ff4a3a;
    --stop-low:#c8160c;
    --knob-light:#f2f2f2;
    --knob-dark:#8e8e8e;
  }
  *{box-sizing:border-box;margin:0;padding:0}
  html,body{width:1200px;height:800px;overflow:hidden}
  body{
    background:linear-gradient(180deg,var(--bg-top) 0%,var(--bg-bottom) 100%);
    font-family:"Arimo",Arial,sans-serif;
    color:var(--white);
    position:relative;
  }
  .status-bar{position:absolute;left:0;top:0;width:1200px;height:52px;background:#000;}
  .status-bar .carrier{position:absolute;left:72px;top:9px;font-size:28px;font-weight:700}
  .status-bar .clock{position:absolute;left:0;width:1200px;top:9px;text-align:center;font-size:29px;font-weight:700}
  .status-bar svg{position:absolute}

  .lcd{
    position:absolute;left:60px;top:107px;width:1062px;height:110px;
    border-radius:16px;border:3px solid var(--frame);
    background-color:var(--lcd);
    background-image:
      linear-gradient(90deg,var(--lcd-grid) 1px,transparent 1px),
      linear-gradient(0deg,var(--lcd-grid) 1px,transparent 1px);
    background-size:17.5px 17.5px;
    box-shadow:0 6px 0 #d8d8d8 inset,0 4px 0 #8a8a8a;
    display:flex;align-items:flex-end;justify-content:center;padding-bottom:8px;
    color:var(--ink);
  }
  .lcd .value{font-family:"Orbitron",sans-serif;font-weight:500;font-size:82px;line-height:1;letter-spacing:2px}
  .lcd .unit{font-family:"Orbitron",sans-serif;font-weight:700;font-size:30px;margin-left:4px;margin-bottom:6px}

  .keypad{
    position:absolute;left:60px;top:243px;width:1068px;height:243px;
    border-radius:14px;border:3px solid var(--frame);overflow:hidden;
    display:grid;grid-template-columns:repeat(6,1fr);grid-template-rows:1fr 1fr;
    box-shadow:0 4px 0 #8a8a8a;
  }
  .key{
    display:flex;align-items:center;justify-content:center;
    font-family:"Orbitron",sans-serif;font-weight:500;font-size:56px;color:var(--ink);
    background:linear-gradient(180deg,var(--key-top) 0%,var(--key-mid) 42%,var(--key-low) 52%,var(--key-low) 100%);
    border-right:2px solid var(--key-line);border-bottom:2px solid var(--key-line);
  }
  .key:nth-child(6n){border-right:none}
  .key:nth-child(n+7){border-bottom:none}
  .key.is-down{background:linear-gradient(180deg,var(--active-top) 0%,#ee5a1e 50%,var(--active-low) 100%)}

  .slider-track{
    position:absolute;left:60px;top:518px;width:1070px;height:36px;border-radius:18px;
    border:3px solid #9a9a9a;
    background:linear-gradient(180deg,var(--key-top) 0%,var(--key-mid) 45%,var(--key-low) 55%,var(--key-mid) 100%);
  }
  .knob{
    position:absolute;border-radius:50%;
    background:radial-gradient(circle at 50% 55%,var(--knob-dark) 0%,#cfcfcf 45%,var(--knob-light) 70%,#9c9c9c 100%);
    box-shadow:0 2px 4px rgba(0,0,0,.6);
  }
  .slider-knob{left:476px;top:506px;width:60px;height:60px}

  .label{position:absolute;font-size:28px;font-weight:700;color:var(--white)}
  .wobble-label{left:68px;top:598px}
  .pink-label{left:499px;top:598px}
  .sweep-label{left:773px;top:598px}

  .toggle{
    position:absolute;left:63px;top:638px;width:164px;height:60px;border-radius:30px;
    border:3px solid #9a9a9a;
    background:linear-gradient(180deg,var(--key-top) 0%,var(--key-mid) 45%,var(--key-low) 55%,var(--key-mid) 100%);
    color:var(--ink);font-weight:700;font-size:26px;
    display:flex;align-items:center;padding-left:74px;
  }
  .toggle .knob{left:-3px;top:-3px;width:60px;height:60px}

  .mode-bar{
    position:absolute;left:440px;top:638px;width:520px;height:60px;border-radius:14px;
    border:3px solid #9a9a9a;overflow:hidden;
    background:linear-gradient(180deg,var(--key-low) 0%,var(--key-mid) 55%,var(--key-top) 100%);
    color:var(--ink);font-weight:700;font-size:36px;
  }
  .mode-bar .mode{position:absolute;top:8px}
  .mode-bar .p{left:110px}
  .mode-bar .s{left:357px}
  .mode-bar svg{position:absolute;left:0;top:0}

  .stop{position:absolute;left:922px;top:582px}
  .stop-text{position:absolute;left:975px;top:621px;font-size:38px;font-weight:700;color:#111}
</style>
</head>
<body>
  <header class="status-bar">
    <svg width="52" height="52" viewBox="0 0 52 52" style="left:16px;top:0">
      <rect x="2" y="28" width="6" height="8" fill="#fff"/>
      <rect x="11" y="23" width="6" height="13" fill="#fff"/>
      <rect x="20" y="18" width="6" height="18" fill="#fff"/>
      <rect x="29" y="13" width="6" height="23" fill="#fff"/>
    </svg>
    <span class="carrier">NETRA</span>
    <svg width="40" height="32" viewBox="0 0 40 32" style="left:163px;top:10px">
      <path d="M3 11 A24 24 0 0 1 37 11" stroke="#fff" stroke-width="5" fill="none"/>
      <path d="M9 18 A16 16 0 0 1 31 18" stroke="#fff" stroke-width="5" fill="none"/>
      <path d="M20 30 L13 23 A10 10 0 0 1 27 23 Z" fill="#fff"/>
    </svg>
    <span class="clock">12:34 PM</span>
    <svg width="50" height="26" viewBox="0 0 50 26" style="left:1138px;top:13px">
      <rect x="1.5" y="1.5" width="42" height="23" rx="4" stroke="#fff" stroke-width="3" fill="none"/>
      <rect x="5" y="5" width="35" height="16" fill="#fff"/>
      <rect x="45" y="8" width="4" height="10" fill="#fff"/>
    </svg>
  </header>

  <section class="lcd">
    <span class="value">32.7</span><span class="unit">HZ</span>
  </section>

  <section class="keypad">
    <div class="key is-down">20</div><div class="key">30</div><div class="key">40</div>
    <div class="key">50</div><div class="key">60</div><div class="key">70</div>
    <div class="key">80</div><div class="key">90</div><div class="key">100</div>
    <div class="key">150</div><div class="key">250</div><div class="key">300</div>
  </section>

  <div class="slider-track"></div>
  <div class="knob slider-knob"></div>

  <span class="label wobble-label">+10 Hz Wobble</span>
  <div class="toggle"><div class="knob"></div>OFF</div>

  <span class="label pink-label">Pink Noise</span>
  <span class="label sweep-label">Sweep</span>
  <div class="mode-bar">
    <svg width="520" height="60"><line x1="270" y1="0" x2="238" y2="60" stroke="#e8860c" stroke-width="2"/></svg>
    <span class="mode p">P</span>
    <span class="mode s">S</span>
  </div>

  <svg class="stop" width="206" height="114" viewBox="0 0 206 114">
    <defs>
      <linearGradient id="stopFill" x1="0" y1="0" x2="0" y2="1">
        <stop offset="0" stop-color="#ff6a58"/>
        <stop offset=".5" stop-color="#e82a1c"/>
        <stop offset="1" stop-color="#c8160c"/>
      </linearGradient>
    </defs>
    <path d="M40 4 H186 Q202 4 202 20 V94 Q202 110 186 110 H4 Z" fill="url(#stopFill)" stroke="#555" stroke-width="3" stroke-linejoin="round"/>
  </svg>
  <span class="stop-text">STOP</span>
</body>
</html>
```